Wordpress theme for new e-commerce tropical furniture manufacturing business

We want to develop a Wordpress theme to suit our new Reefline Furniture website currently under development, business details as below.
Please see attached logo design for ideas of the design. This logo will be used as - letterhead, business cards, furniture labels etc.
We are a small Australian family business that provides products as below:
- Hand Crafted, Creative Tropical design Furniture,
(manufacture and sales).
- Specializing in mirror- wall art
- One off – designs 'made to order'.
- Individually badged pieces, each with an identification production number.
Materials used that may be incorporated in the 'web theme designs' are: Bamboo, Wood, Waves, Ocean, Shells, Tropical flowers (eg; Hibiscus, Frangipani, Heliconias, Stralitzias), Palms,Pandanus & Stone etc. etc.
Industry/Entity Type
E-Commerce
Colors
Designer to choose colors to be used in the design.
Look and feel
Each slider illustrates characteristics of the customer's brand and the style your logo design should communicate.

```html
<!DOCTYPE html>
<html lang="en">
<head>
<meta charset="utf-8">
<title>Reefline Furniture</title>
<link rel="stylesheet" href="https://fonts.googleapis.com/css2?family=Dancing+Script:wght@500;600;700&display=swap">
<style>
  :root {
    --ocean-deep: #12608a;
    --ocean-mid: #1f86b4;
    --ocean-light: #45b3d8;
    --bamboo-dark: #b8702f;
    --bamboo-mid: #d99152;
    --bamboo-light: #f2bd82;
    --bamboo-line: rgba(110, 58, 20, .55);
    --cream: #fdf0e1;
    --ink: #6b5445;
    --ink-dark: #4f3c30;
    --white: #ffffff;
    --icon-blue: #2a7fb0;
    --btn-top: #ffffff;
    --btn-bottom: #e6ddd6;
  }
  * { box-sizing: border-box; margin: 0; padding: 0; }
  html, body { width: 1200px; height: 1000px; overflow: hidden; }
  body {
    position: relative;
    background:
      repeating-linear-gradient(172deg, rgba(255,255,255,0) 0 9px, rgba(255,255,255,.07) 10px 12px, rgba(0,40,70,.08) 13px 15px, rgba(255,255,255,0) 16px 26px),
      repeating-linear-gradient(8deg, rgba(255,255,255,0) 0 14px, rgba(120,210,240,.10) 15px 18px, rgba(255,255,255,0) 19px 31px),
      radial-gradient(ellipse at 15% 30%, var(--ocean-light), transparent 55%),
      radial-gradient(ellipse at 88% 70%, var(--ocean-light), transparent 50%),
      linear-gradient(180deg, var(--ocean-mid), var(--ocean-deep));
    font-family: "Dancing Script", cursive;
    color: var(--ink);
  }
  .page {
    position: absolute; left: 195px; top: 22px; width: 815px; height: 1000px;
    background:
      repeating-linear-gradient(90deg,
        transparent 0 13px, var(--bamboo-line) 13px 14px, rgba(255,225,180,.35) 14px 16px,
        transparent 16px 31px, var(--bamboo-line) 31px 32px, rgba(255,225,180,.3) 32px 34px,
        transparent 34px 52px, var(--bamboo-line) 52px 53px, rgba(255,225,180,.35) 53px 55px,
        transparent 55px 67px),
      repeating-linear-gradient(90deg, rgba(150,80,30,.18) 0 4px, transparent 4px 9px, rgba(255,230,190,.15) 9px 11px, transparent 11px 17px),
      linear-gradient(90deg, var(--bamboo-dark), var(--bamboo-mid) 15%, var(--bamboo-light) 45%, var(--bamboo-mid) 80%, var(--bamboo-dark));
    box-shadow: 0 0 24px rgba(0,0,0,.45);
  }
  .site-header { position: absolute; left: 0; top: 0; width: 815px; height: 154px; }
  .brand {
    position: absolute; left: 18px; top: 26px; width: 312px; height: 136px;
    border-radius: 50%; background: var(--white); border: 2px solid #cfc5bb;
    box-shadow: 0 3px 8px rgba(0,0,0,.4);
    display: flex; align-items: center; justify-content: center; z-index: 2;
  }
  .brand-name { font-size: 36px; font-weight: 700; color: var(--icon-blue); }
  .social { position: absolute; left: 538px; top: 24px; display: flex; gap: 12px; }
  .social-item {
    width: 31px; height: 31px; background: var(--icon-blue);
    border: 3px solid var(--white); box-shadow: 0 0 0 1px var(--icon-blue);
    display: flex; align-items: center; justify-content: center;
  }
  .cart {
    position: absolute; left: 718px; top: 9px; width: 63px; height: 57px;
    border-radius: 10px; background: #e8ddd3; border: 3px solid #6e5a4b;
    display: flex; align-items: center; justify-content: center;
  }
  .main-nav { position: absolute; left: 352px; top: 83px; display: flex; }
  .nav-link {
    display: block; height: 35px; line-height: 33px; text-align: center;
    font-size: 21px; font-weight: 700; color: var(--ink); text-decoration: none;
    background: linear-gradient(var(--btn-top), var(--btn-bottom));
    border: 1.5px solid var(--ink-dark); border-radius: 50% / 50%;
    box-shadow: 0 2px 4px rgba(0,0,0,.35);
  }
  .hero {
    position: absolute; left: 0; top: 154px; width: 815px; height: 238px;
    box-shadow: 0 8px 12px rgba(60,30,10,.55);
    background:
      linear-gradient(180deg, transparent 0 50%, rgba(90,45,20,.0) 50%, rgba(120,60,25,.85) 62%, rgba(150,80,35,.9) 80%, rgba(90,50,25,.8) 100%) 180px 0 / 480px 100% no-repeat,
      linear-gradient(180deg, #2a3f6e 0%, #4f6fa8 18%, #9a8fb8 26%, #2f6eb5 34%, #1d4f8a 60%, #15305a 100%) 0 0 / 260px 100% no-repeat,
      linear-gradient(180deg, #5a6d80 0%, #8fa0ae 40%, #6b5a48 100%) 260px 0 / 250px 100% no-repeat,
      linear-gradient(180deg, #efe8de 0%, #e6ded2 40%, #2a2622 45%, #3a332c 55%, #cfc8bd 60%, #bdb5aa 100%) 510px 0 / 305px 100% no-repeat;
  }
  .content {
    position: absolute; left: 23px; top: 423px; width: 770px; height: 600px;
    background: var(--cream); box-shadow: 0 0 10px rgba(0,0,0,.35);
  }
  .shell-mark {
    position: absolute; left: 25px; top: 16px; width: 72px; height: 66px;
    background: radial-gradient(circle at 50% 90%, #f7eee4, #d8c9ba);
    border-radius: 50% 50% 40% 40%;
  }
  .page-title {
    position: absolute; left: 115px; top: 6px; width: 627px; text-align: center;
    font-size: 41px; font-weight: 700; color: var(--ink);
  }
  .title-rule { position: absolute; left: 115px; top: 62px; width: 627px; height: 2px; background: var(--ink); }
  .category { position: absolute; top: 121px; width: 200px; text-align: center; }
  .category-photo {
    width: 150px; height: 150px; margin: 0 auto;
    box-shadow: 3px 4px 8px rgba(0,0,0,.45);
  }
  .category-name { margin-top: 12px; font-size: 28px; font-weight: 700; color: var(--ink); }
  .intro {
    position: absolute; left: 69px; top: 343px; width: 640px;
    font-size: 21px; font-weight: 700; line-height: 24.4px; color: var(--ink);
  }
</style>
</head>
<body>
  <div class="page">
    <header class="site-header">
      <div class="brand"><span class="brand-name">Reefline Furniture</span></div>
      <div class="social">
        <span class="social-item"></span>
        <span class="social-item">
          <svg width="22" height="16" viewBox="0 0 22 16"><rect x="1" y="1" width="20" height="14" fill="none" stroke="#fff" stroke-width="2"/><path d="M1 1 L11 9 L21 1" fill="none" stroke="#fff" stroke-width="2"/></svg>
        </span>
        <span class="social-item"></span>
        <span class="social-item"></span>
      </div>
      <div class="cart">
        <svg width="42" height="36" viewBox="0 0 42 36"><path d="M2 4 H9 L14 24 H34 L39 9 H11" fill="none" stroke="#6e5a4b" stroke-width="3" stroke-linejoin="round"/><circle cx="16" cy="31" r="3" fill="#6e5a4b"/><circle cx="32" cy="31" r="3" fill="#6e5a4b"/></svg>
      </div>
      <nav class="main-nav">
        <a class="nav-link" href="#" style="width:104px">Catalog</a>
        <a class="nav-link" href="#" style="width:103px;margin-left:12px">Sets</a>
        <a class="nav-link" href="#" style="width:104px;margin-left:6px">About</a>
        <a class="nav-link" href="#" style="width:104px;margin-left:11px">Contact</a>
      </nav>
    </header>

    <div class="hero" role="img" aria-label="Tropical villa dining room with a timber slab table and benches overlooking the ocean at dusk"></div>

    <main class="content">
      <div class="shell-mark" role="img" aria-label="Scallop shell ornament"></div>
      <h1 class="page-title">Reefline Furniture</h1>
      <div class="title-rule"></div>

      <div class="category" style="left:55px">
        <div class="category-photo" role="img" aria-label="Carved timber bedroom set" style="background:linear-gradient(180deg,#4a3626 0%,#8a7256 30%,#c9b89a 55%,#7a5a3c 75%,#3e2a1c 100%)"></div>
        <div class="category-name">Bedroom Sets</div>
      </div>
      <div class="category" style="left:284px">
        <div class="category-photo" role="img" aria-label="Custom timber framed wall mirror" style="background:radial-gradient(ellipse 28% 38% at 50% 45%,#e4e4e2,#9a9a98 70%,#6a4228 78%,transparent 86%),linear-gradient(160deg,#d8ceb0,#c2b492 60%,#8a7a58)"></div>
        <div class="category-name">Custom Mirrors</div>
      </div>
      <div class="category" style="left:511px">
        <div class="category-photo" role="img" aria-label="Timber kitchen with stone bench" style="background:linear-gradient(180deg,#c88a4a 0%,#e0b070 22%,#8a6a4a 45%,#5a4a3e 70%,#3a3028 100%)"></div>
        <div class="category-name">Kitchen Sets</div>
      </div>

      <p class="intro">Lorem ipsum dolor sit amet, consectetur adipiscing elit. Aenean luctus feugiat consectetur. Etiam aliquet urna id turpis ullamcorper aliquam. Sed congue sapien vel lorem faucibus elementum. Aenean vitae lacus lorem. Maecenas rutrum libero et mi lacinia pulvinar. Donec faucibus lacus elementum urna posuere, eget rutrum arcu semper. Donec rutrum libero tellus, pretium faucibus lorem volutpat vel. Maecenas imperdiet justo est, non tempor elit egestas eu. Nunc congue mattis scelerisque. Vestibulum quis volutpat libero. Donec accumsan nulla et est pellentesque, eu bibendum urna tempus. Fusce non est at elit iaculis luctus. Nunc</p>
    </main>
  </div>
</body>
</html>
```